Need design for Vinyl window signs

I need Vinyl window sign to cover my front retail pharmacy window. Not the whole window area i want there to be open areas so people can still see inside.
Attached is the pic of front door and also the logo which contains the colors we want to use. The width of the door is about 14ft wide and 7ft high and its 3 sections. The middle section the door is 36 inch.

And the vinyl graphic should include the following info:
Maplecrest Commons pharmacy
Caring for you, Caring for the community

Wellness starts here!
Locally owned independent pharmacy
No wait
Same Copay as chains
Free local delivery

We do prescriptions, private consultations, compounding, immunizations, travel health and other clinical services

We also provide free blood pressure, blood glucose and blood oxygen testing everyday.
No appointments necessary.

Write Pharmacy in different languages: Spanish, Farsi, Hebrew, Russian

Phone: 555-206-3948

Hours:
M- F 9-6
Sat and sun and major Holliday: closed

Target Market(s)

Patients: People seeking medication or health advice. Caregivers: Those caring for others who need prescriptions. Health-Conscious Individuals: People interested in preventive health measures. Chronic Condition Sufferers: Individuals managing ongoing health issues. Healthcare Professionals: Doctors and nurses who may refer patients to pharmacists.

Industry/Entity Type

Retail pharmacy

Font styles to use
Sans Serif

Colors
0054AA
0677BA
7BADD7
CADEEF
E8F1F8
00AB8E
00BBA5
67D7C9
C6EFE9
E9F9F6

Requirements
Must have
• At least 3 sections for each window left side and right side and middle area, must have Green and blue color to match my logo see attached.
Nice to have
• Like to see a pics or two of people maybe seniors and younger adults enjoying their time

```html
<!DOCTYPE html>
<html lang="en">
<head>
<meta charset="utf-8">
<title>Maplecrest Commons Pharmacy – Window Vinyl</title>
<link href="https://fonts.googleapis.com/css2?family=Anton&family=Arimo:wght@400;700&family=Tinos&family=Vazirmatn:wght@400&display=swap" rel="stylesheet">
<style>
  :root{
    --page:#ffffff;
    --frame:#2a2a2a;
    --frame-line:#111111;
    --door:#000000;
    --green:#10ad4b;
    --green-light:#8cc63f;
    --blue:#0a72bb;
    --blue-bright:#1a8fe0;
    --yellow:#f6e51b;
    --white:#ffffff;
    --glass-top:#5a5d5c;
    --glass-bottom:#3c3f3e;
  }
  *{margin:0;padding:0;box-sizing:border-box}
  html,body{width:1200px;height:725px;overflow:hidden;background:var(--page)}
  body{position:relative;font-family:'Arimo',Arial,sans-serif;color:var(--white)}
  .storefront{position:absolute;left:87px;top:86px;width:1020px;height:561px;background:var(--frame)}
  .window-line{position:absolute;left:108px;top:119px;width:974px;height:496px;border:1px solid var(--frame-line)}
  .door{position:absolute;left:475px;top:140px;width:236px;height:507px;background:var(--door);border-left:4px solid #222;border-right:4px solid #222}
  .panel{position:absolute;top:141px;width:343px;height:436px;background:var(--blue);overflow:hidden}
  .panel--left{left:129px}
  .panel--right{left:715px;top:142px;height:435px}
  .panel svg{position:absolute;left:0;top:0}
  .txt{position:absolute;left:0;width:100%;text-align:center;white-space:nowrap}
  .headline{font-family:'Anton',Impact,sans-serif;text-shadow:1px 1px 0 rgba(0,0,0,.35)}
  .bold{font-weight:700}
  .badge{position:absolute;left:26px;top:172px;width:88px;height:88px;border-radius:50%;background:var(--green);border:4px solid var(--white);text-align:center;font-family:'Anton',Impact,sans-serif;line-height:1}
  .pill{position:absolute;left:48px;top:293px;width:246px;height:20px;border-radius:10px;background:var(--green);border:1px solid var(--white);text-align:center;font-weight:700;font-size:14px;line-height:18px}
  .we-do{display:inline-block;background:var(--yellow);color:var(--blue);border-radius:5px;padding:0 3px;font-size:8px;margin-right:4px}
  .accent{color:var(--yellow)}
  .lang-band{position:absolute;left:0;top:398px;width:100%;height:38px;background:var(--green);border-top:3px solid #e8e8e8;font-size:21px;line-height:36px;text-align:center;direction:ltr}
  .farsi{font-family:'Vazirmatn',sans-serif}
  .lang-label{position:absolute;font-family:'Tinos','Times New Roman',serif;font-size:9.5px;color:var(--white)}
  .glass{position:absolute;left:500px;top:157px;width:186px;height:220px;background:linear-gradient(180deg,var(--glass-top),var(--glass-bottom))}
  .brand-dot{position:absolute;left:555px;top:200px;width:70px;height:70px;border-radius:50%;background:var(--green);border:4px solid var(--white)}
  .brand-name{position:absolute;left:500px;width:186px;text-align:center;font-weight:700;color:var(--blue-bright);white-space:nowrap}
  .glass-note{position:absolute;left:500px;top:356px;width:186px;text-align:center;font-size:11px;color:#e6e6e6}
  .handle{position:absolute;left:691px;top:316px;width:8px;height:50px;border-radius:4px;background:var(--white)}
  .hours{position:absolute;left:500px;top:390px;width:186px;height:144px;background:var(--blue)}
  .hours-rule{position:absolute;top:39px;width:38px;height:1px;background:var(--white)}
  .hours-bar{position:absolute;left:27px;top:49px;width:130px;height:14px;background:var(--green);font-size:10.5px;line-height:14px;text-align:center}
  .phone-band{position:absolute;left:500px;top:539px;width:186px;height:38px;background:var(--green);text-align:center;font-weight:700;font-size:23px;line-height:38px}
  .phone-band svg{vertical-align:-3px;margin-right:5px}
  .test-pill{position:absolute;top:336px;width:88px;height:24px;border-radius:12px;background:var(--blue);border:1.5px solid var(--white);box-shadow:1px 2px 2px rgba(0,0,0,.3)}
  .test-pill .dot{position:absolute;left:1px;top:1px;width:19px;height:19px;border-radius:50%;background:var(--green);border:1.5px solid var(--white)}
  .test-pill span{position:absolute;left:20px;right:0;top:2px;text-align:center;font-size:8.5px;font-weight:700;line-height:9px}
</style>
</head>
<body>
<div class="storefront"></div>
<div class="window-line"></div>
<div class="door"></div>

<!-- Left window -->
<section class="panel panel--left">
  <svg width="343" height="436" viewBox="0 0 343 436">
    <defs>
      <linearGradient id="headLeft" x1="0" y1="0" x2="0" y2="1">
        <stop offset="0" stop-color="#8cc63f"/><stop offset="1" stop-color="#10ad4b"/>
      </linearGradient>
      <linearGradient id="photoFamily" x1="0" y1="0" x2="1" y2="1">
        <stop offset="0" stop-color="#cfd8cf"/><stop offset=".5" stop-color="#e9e4dc"/><stop offset="1" stop-color="#9aa8b8"/>
      </linearGradient>
      <clipPath id="clipLeft"><rect x="0" y="102" width="343" height="300"/></clipPath>
    </defs>
    <rect x="0" y="102" width="343" height="25" fill="#000"/>
    <g clip-path="url(#clipLeft)">
      <circle cx="173" cy="93" r="160" fill="#10ad4b"/>
      <circle cx="173" cy="93" r="154" fill="url(#photoFamily)" role="img" aria-label="Photo of a smiling family with two children and a dog relaxing on a sofa"/>
    </g>
    <rect x="0" y="0" width="343" height="102" fill="url(#headLeft)"/>
  </svg>
  <div class="txt headline" style="top:20px;font-size:27px">WELLNESS</div>
  <div class="txt headline" style="top:49px;font-size:36px">STARTS HERE!</div>
  <div class="badge">
    <svg width="26" height="16" viewBox="0 0 26 16" style="position:static;margin-top:6px"><rect x="1" y="2" width="15" height="9" fill="none" stroke="#fff" stroke-width="1.6"/><path d="M16 5h5l3 3v3h-8z" fill="none" stroke="#fff" stroke-width="1.6"/><circle cx="6" cy="13" r="2" fill="#fff"/><circle cx="20" cy="13" r="2" fill="#fff"/></svg>
    <div style="font-size:22px">FREE</div>
    <div style="font-size:12px;margin-top:1px">LOCAL</div>
    <div style="font-size:12px;margin-top:1px">DELIVERY</div>
  </div>
  <div class="txt bold" style="top:265px;font-size:20px;left:-14px">LOCALLY OWNED</div>
  <div class="pill">INDEPENDENT PHARMACY</div>
  <div class="txt bold" style="top:320px;font-size:12px;left:6px">NO WAIT &nbsp;|&nbsp; SAME COPAY AS CHAINS</div>
  <div class="txt bold" style="top:357px;font-size:9.5px;left:8px"><span class="we-do">WE DO</span><span class="accent">•</span> PRESCRIPTIONS <span class="accent">•</span> PRIVATE CONSULTATIONS</div>
  <div class="txt bold" style="top:370px;font-size:9.5px;left:14px"><span class="accent">•</span> COMPOUNDING <span class="accent">•</span> IMMUNIZATIONS <span class="accent">•</span> TRAVEL HEALTH</div>
  <div class="txt bold" style="top:382px;font-size:9.5px;left:5px">AND <span class="accent">OTHER CLINICAL SERVICES</span></div>
  <div class="lang-band">FARMACIA &nbsp;&nbsp;| &nbsp;&nbsp;Аптека</div>
</section>
<div class="lang-label" style="left:172px;top:588px">Spanish,</div>
<div class="lang-label" style="left:317px;top:588px">Russian</div>

<!-- Door -->
<div class="glass" role="img" aria-label="Transparent glass showing the pharmacy interior"></div>
<div class="brand-dot"></div>
<div class="brand-name" style="top:282px;font-size:13px">MAPLECREST COMMONS</div>
<div class="brand-name" style="top:296px;font-size:24px">PHARMACY</div>
<div class="glass-note">TRANSPERANT GLASS</div>
<div class="handle"></div>
<div class="hours">
  <div class="hours-rule" style="left:28px"></div>
  <div class="hours-rule" style="left:120px"></div>
  <div class="txt bold" style="top:33px;font-size:12px">HOURS</div>
  <div class="hours-bar">MON- FRI &nbsp;9AM - 6PM</div>
  <div class="txt bold" style="top:78px;font-size:12px">SAT AND SUN</div>
  <div class="txt bold" style="top:91px;font-size:12px">AND MAJOR HOLLIDAY</div>
  <div class="txt bold" style="top:107px;font-size:18px">CLOSED</div>
</div>
<div class="phone-band"><svg width="14" height="19" viewBox="0 0 14 19"><rect x="2" y="1" width="10" height="17" rx="2" fill="none" stroke="#fff" stroke-width="2"/><rect x="5" y="14" width="4" height="1.6" fill="#fff"/></svg>555-206-3948</div>

<!-- Right window -->
<section class="panel panel--right">
  <svg width="343" height="435" viewBox="0 0 343 435">
    <defs>
      <linearGradient id="headRight" x1="0" y1="0" x2="0" y2="1">
        <stop offset="0" stop-color="#8cc63f"/><stop offset="1" stop-color="#10ad4b"/>
      </linearGradient>
      <linearGradient id="photoCare" x1="0" y1="0" x2="1" y2="1">
        <stop offset="0" stop-color="#e6e2de"/><stop offset=".5" stop-color="#f1ece8"/><stop offset="1" stop-color="#b9c4d8"/>
      </linearGradient>
      <clipPath id="clipRight"><rect x="0" y="101" width="343" height="300"/></clipPath>
    </defs>
    <rect x="0" y="101" width="343" height="25" fill="#000"/>
    <g clip-path="url(#clipRight)">
      <circle cx="175" cy="104" r="160" fill="#10ad4b"/>
      <circle cx="175" cy="104" r="153" fill="url(#photoCare)" role="img" aria-label="Photo of a clinician measuring an older man's blood pressure while an older woman looks on"/>
    </g>
    <rect x="0" y="0" width="343" height="101" fill="url(#headRight)"/>
  </svg>
  <div class="txt headline" style="top:24px;font-size:33px">CARING FOR YOU,</div>
  <div class="txt headline" style="top:61px;font-size:20px">CARING FOR THE COMMUNITY</div>
  <div class="txt bold" style="top:270px;font-size:18px;text-shadow:1px 1px 0 rgba(0,0,0,.3)">EVERYDAY WE PROVIDE</div>
  <div class="txt bold" style="top:289px;font-size:33px;text-shadow:1px 1px 0 rgba(0,0,0,.3)">FREE TESTING</div>
  <div class="test-pill" style="left:27px"><div class="dot"></div><span>BLOOD<br>PRESSURE</span></div>
  <div class="test-pill" style="left:126px"><div class="dot"></div><span>BLOOD<br>GLUCOSE</span></div>
  <div class="test-pill" style="left:223px"><div class="dot"></div><span>BLOOD<br>OXYGEN</span></div>
  <div class="txt" style="top:371px;font-size:13px">NO APPOINTMENTS NECESSARY</div>
  <div class="lang-band"><bdi>בֵּית מִרְקַחַת</bdi> &nbsp;&nbsp;| &nbsp;&nbsp;<bdi class="farsi">داروخانه</bdi></div>
</section>
<div class="lang-label" style="left:769px;top:585px">Hebrew</div>
<div class="lang-label" style="left:921px;top:585px">Farsi,</div>
</body>
</html>
```